Wordpress Design Project - Development Company

We need a website for our Developments company "KT Developments". I would like to use Wordpress for its simplicity to update and added features.
We develop/build and sell Townhouses/Houses and Land around Brisbane, Qld. Initially we require a Web presence with no advanced features. We will develop the user logins and other features at a future point in time. We are undecided on having a single page with most of the detail or to have more detail on linked pages, we will review the options put forward. We have added a Sitemap and possible Frontpage sketch
Some sites for examples we have thought work similar and well:
http://www.ferncastle.com.au/index.htm
http://tallwillowplains.com.au/
http://www.mqholloway.com.au
http://coralframe.com.au/
http://www.pelham.com.au/queensland.aspx
http://www.meridale.com.au/
I've attached our newly created Business Cards and we are also working on a logo for the company within the next couple of days which may or may not be the same as the Business Card
Any questions please ask
Updates
Please update the main picture on your webpages to the attached so we can compare equally http://files.filevaultex.com/u/50927361/Img1c.jpg
Target Market(s)
Townhouse/House/Land buyers & Salespeople
Industry/Entity Type
Business
Look and feel
Each slider illustrates characteristics of the customer's brand and the style your logo design should communicate.

```html
<!DOCTYPE html>
<html lang="en">
<head>
<meta charset="utf-8">
<title>KT Developments P/L</title>
<link rel="stylesheet" href="https://fonts.googleapis.com/css2?family=Arimo:wght@400;700&display=swap">
<style>
:root{
  --page:#000;
  --panel-top:#2c2c2c;
  --panel-bottom:#0d0d0d;
  --panel-line:#3c3c3c;
  --text-light:#fff;
  --text-muted:#8a8a8a;
  --text-dim:#6f6f6f;
  --header-top:#ffffff;
  --header-bottom:#d6d6d6;
  --ink:#111;
  --field:#fff;
  --field-text:#9a9a9a;
  --divider:#262626;
}
*{box-sizing:border-box;margin:0;padding:0}
html,body{width:1133px;height:1200px;overflow:hidden;background:var(--page)}
body{position:relative;font-family:"Arimo",Arial,sans-serif;color:var(--text-light)}
.abs{position:absolute}

.site-header{left:0;top:0;width:1133px;height:95px;background:linear-gradient(var(--header-top),var(--header-bottom));border-bottom:2px solid #9a9a9a}
.brand{left:52px;top:22px;display:flex;align-items:center;gap:26px;color:var(--ink)}
.brand-mark{font-size:58px;font-weight:700;letter-spacing:-2px;line-height:1}
.brand-name{font-size:31px;letter-spacing:1.5px;font-weight:400}
.header-search{left:895px;top:33px;width:198px;height:35px;display:flex;border-radius:3px;overflow:hidden;border:1px solid #555}
.header-search span{flex:1;background:#25262b;color:#fff;font-size:13px;padding:11px 15px}
.header-search i{width:34px;background:#6b6c70;display:flex;align-items:center;justify-content:center}

.main-nav{left:52px;top:103px;height:44px;display:flex;align-items:center}
.home-btn{width:42px;height:42px;border-radius:50%;border:2px solid #8a8a8a;background:radial-gradient(#555,#111);display:flex;align-items:center;justify-content:center;margin-right:26px}
.main-nav a{color:#fff;text-decoration:none;font-size:13px;font-weight:700;margin-right:32px}
.contact-strip{left:649px;top:98px;width:445px;height:56px;background:linear-gradient(#2a2a2a,#101010);border:1px solid #3a3a3a;display:flex;align-items:center;padding:0 8px}
.contact-strip .tagline{color:var(--text-muted);font-size:16px;flex:1}
.contact-strip .phone{font-size:18px;font-weight:700;display:flex;align-items:center;gap:10px}

.hero{left:52px;top:158px;width:1042px;height:376px;border:3px solid #fff;background:linear-gradient(#8fb0d6 0%,#bcd0e2 32%,#a9a596 58%,#6f7470 78%,#7a7e78 100%)}
.hero-arrow{top:160px}
.hero-dots{right:12px;bottom:12px;display:flex;gap:7px}
.hero-dots b{width:14px;height:14px;border:1px solid #fff;display:block}
.hero-dots b.on{background:#fff}

.property-search{left:52px;top:560px;width:1042px;height:47px;background:linear-gradient(#2f2f2f,#0f0f0f);border:1px solid #3d3d3d;display:flex;align-items:center;padding-left:11px}
.property-search h2{font-size:18px;font-weight:700;letter-spacing:.3px;width:220px}
.select{width:126px;height:24px;background:var(--field);color:var(--field-text);font-size:12px;padding:5px 9px;margin-right:10px;position:relative}
.select svg{position:absolute;right:6px;top:7px}
.submit{margin-left:10px;width:97px;height:25px;border:1px solid #888;background:linear-gradient(#3a3a3a,#050505);font-size:12px;font-weight:700;text-align:center;line-height:23px;letter-spacing:.5px}

.panel-head{height:47px;border:1px solid var(--panel-line);border-radius:3px;background:linear-gradient(var(--panel-top),var(--panel-bottom));display:flex;align-items:center;font-size:18px}
.badge{width:56px;height:56px;border-radius:50%;border:2px solid #888;background:radial-gradient(#444,#0a0a0a);font-size:17px;font-weight:700;display:flex;align-items:center;justify-content:center;margin:0 12px 0 10px;color:#e8e8e8}
.copy{font-size:12.4px;line-height:19.4px;color:var(--text-dim);text-align:justify}
.more-btn{width:72px;height:30px;border:1px solid #444;border-radius:3px;background:linear-gradient(#3a3a3a,#151515);color:#888;font-size:14px;font-weight:700;text-align:center;line-height:28px}
.news-item{display:flex;gap:12px;margin-bottom:12px}
.news-date{width:38px;font-size:11px;font-weight:700;flex:none}
.news-date i{display:block;width:7px;height:44px;background:linear-gradient(#fff 70%,#444 70%);margin:2px 0 0 31px;border-top:1px solid #fff}
.tour-photo{left:764px;top:705px;width:330px;height:151px;border:2px solid #fff;border-radius:4px;background:linear-gradient(#9bb9dc 0%,#c8cdc4 45%,#8a8473 75%,#5e5e58 100%)}

.project-list{list-style:none}
.project-list li{height:56px;border-bottom:1px solid var(--divider);position:relative;padding:10px 0 0 32px;font-size:12.6px;font-weight:700;line-height:19.5px}
.project-list li:last-child{border-bottom:none}
.project-list li::before{content:"›";position:absolute;left:12px;top:6px;font-size:18px}
.project-list .details{position:absolute;right:14px;top:33px;color:var(--text-dim);font-size:12.4px}
.project-list .line1{display:block}

.site-footer{left:0;top:1129px;width:1133px;height:71px;border-top:1px solid #222}
.copyright{left:53px;top:20px;font-size:13px}
.social{right:36px;top:20px;display:flex;align-items:center;gap:10px;font-size:13px;font-weight:700}
.social b{width:17px;height:17px;display:block;border-radius:2px}
</style>
</head>
<body>

<header class="site-header abs">
  <div class="brand abs"><span class="brand-mark">KT</span><span class="brand-name">Developments P/L</span></div>
  <div class="header-search abs"><span>Search</span><i><svg width="14" height="14" viewBox="0 0 14 14"><circle cx="5.5" cy="5.5" r="4.3" fill="none" stroke="#111" stroke-width="1.8"/><path d="M8.7 8.7L13 13" stroke="#111" stroke-width="2"/></svg></i></div>
</header>

<nav class="main-nav abs">
  <span class="home-btn"><svg width="22" height="20" viewBox="0 0 22 20"><path d="M11 1L1 10h3v9h5v-6h4v6h5v-9h3z" fill="#fff"/></svg></span>
  <a href="#">ABOUT US</a><a href="#">PORTFOLIO</a><a href="#">SERVICES</a><a href="#">BLOG</a><a href="#">CONTACT</a>
</nav>
<div class="contact-strip abs">
  <span class="tagline">Helping you find the way home</span>
  <span class="phone"><svg width="24" height="16" viewBox="0 0 24 16"><path d="M2 5c0-3 20-3 20 0v2h-5V5H7v2H2z" fill="#ddd"/><rect x="5" y="8" width="14" height="8" rx="2" fill="#ddd"/><circle cx="12" cy="12" r="2" fill="#222"/></svg>Call : 1-300 -555-014</span>
</div>

<section class="hero abs" role="img" aria-label="Rendered street of new two-storey townhouses under a blue sky">
  <svg class="hero-arrow abs" style="left:10px" width="24" height="30" viewBox="0 0 24 30"><path d="M18 3L6 15l12 12" fill="none" stroke="#fff" stroke-width="4"/></svg>
  <svg class="hero-arrow abs" style="right:10px" width="24" height="30" viewBox="0 0 24 30"><path d="M6 3l12 12L6 27" fill="none" stroke="#fff" stroke-width="4"/></svg>
  <div class="hero-dots abs"><b class="on"></b><b></b><b></b><b></b></div>
</section>

<form class="property-search abs">
  <h2>SEARCH PROPERTIES</h2>
  <div class="select">Project Type<svg width="14" height="9" viewBox="0 0 14 9"><path d="M1 1l6 6 6-6" fill="none" stroke="#111" stroke-width="2.5"/></svg></div>
  <div class="select">Region<svg width="14" height="9" viewBox="0 0 14 9"><path d="M1 1l6 6 6-6" fill="none" stroke="#111" stroke-width="2.5"/></svg></div>
  <div class="select">Min. Priece<svg width="14" height="9" viewBox="0 0 14 9"><path d="M1 1l6 6 6-6" fill="none" stroke="#111" stroke-width="2.5"/></svg></div>
  <div class="select">Max Price.<svg width="14" height="9" viewBox="0 0 14 9"><path d="M1 1l6 6 6-6" fill="none" stroke="#111" stroke-width="2.5"/></svg></div>
  <div class="select" style="width:141px">Hot Properties<svg width="14" height="9" viewBox="0 0 14 9"><path d="M1 1l6 6 6-6" fill="none" stroke="#111" stroke-width="2.5"/></svg></div>
  <div class="submit">SUBMIT</div>
</form>

<section class="welcome">
  <div class="panel-head abs" style="left:52px;top:635px;width:331px"><span class="badge">KT</span>Welcome KT Developements</div>
  <p class="copy abs" style="left:52px;top:704px;width:331px">Lorem ipsum dolor sit amet, sectetu adip scing varius interdum incid unt quis, libero. Aenean mturpis. Maecenas hendrerit masa laoreet iaculipede mnisl ulamcorper. Tellus er sodales enim, in tincidunt mauris in odio. Massa ac laoreet iaculipede nisl ullamcorper-massa, ac consectetuer feipsum eget pede.</p>
  <div class="more-btn abs" style="left:311px;top:828px">More...</div>
</section>

<section class="news">
  <div class="panel-head abs" style="left:406px;top:635px;width:331px"><span class="badge">KT</span>Our Current News...</div>
  <div class="abs" style="left:408px;top:700px;width:329px">
    <div class="news-item"><div class="news-date">23 Jun<i></i></div><p class="copy">Lorem ipsum dolor sit amet, sectetu adip scing varius interdum incid unt quis, libero. Aenean mturpis. Maecenas hendrerit</p></div>
    <div class="news-item"><div class="news-date">23 Jun<i></i></div><p class="copy">Lorem ipsum dolor sit amet, sectetu adip scing varius interdum incid unt quis, libero. Aenean mturpis. Maecenas hendrerit</p></div>
  </div>
  <div class="more-btn abs" style="left:665px;top:828px">More...</div>
</section>

<section class="tours">
  <div class="panel-head abs" style="left:763px;top:635px;width:331px"><span class="badge">KT</span>Our Project Tours...</div>
  <div class="tour-photo abs" role="img" aria-label="Rendered two-storey townhouse for the project tour"></div>
</section>

<section class="abs" style="left:52px;top:879px;width:331px">
  <div class="panel-head" style="padding-left:14px">Our Current Projects</div>
  <ul class="project-list" style="margin-top:12px">
    <li><span class="line1">Lorem ipsum dolor sit amet, sectetu adip scing</span>varius interdum incid<span class="details">More Details</span></li>
    <li><span class="line1">Lorem ipsum dolor sit amet, sectetu adip scing</span>varius interdum incid<span class="details">More Details</span></li>
    <li><span class="line1">Lorem ipsum dolor sit amet, sectetu adip scing</span>varius interdum incid<span class="details">More Details</span></li>
  </ul>
</section>
<section class="abs" style="left:406px;top:879px;width:331px">
  <div class="panel-head" style="padding-left:14px">Our Completed Projects</div>
  <ul class="project-list" style="margin-top:12px">
    <li><span class="line1">Lorem ipsum dolor sit amet, sectetu adip scing</span>varius interdum incid<span class="details">More Details</span></li>
    <li><span class="line1">Lorem ipsum dolor sit amet, sectetu adip scing</span>varius interdum incid<span class="details">More Details</span></li>
    <li><span class="line1">Lorem ipsum dolor sit amet, sectetu adip scing</span>varius interdum incid<span class="details">More Details</span></li>
  </ul>
</section>
<section class="abs" style="left:763px;top:879px;width:331px">
  <div class="panel-head" style="padding-left:14px">Our&nbsp; Feature Projects</div>
  <ul class="project-list" style="margin-top:12px">
    <li><span class="line1">Lorem ipsum dolor sit amet, sectetu adip scing</span>varius interdum incid<span class="details">More Details</span></li>
    <li><span class="line1">Lorem ipsum dolor sit amet, sectetu adip scing</span>varius interdum incid<span class="details">More Details</span></li>
    <li><span class="line1">Lorem ipsum dolor sit amet, sectetu adip scing</span>varius interdum incid<span class="details">More Details</span></li>
  </ul>
</section>

<footer class="site-footer abs">
  <span class="copyright abs">Copyright Text</span>
  <div class="social abs">OUR SOCIAL&nbsp; CONNECT
    <b style="background:#3b5a9a;margin-left:4px"></b><b style="background:#e9781f"></b><b style="background:#3aa5d8"></b>
  </div>
</footer>

</body>
</html>
```